BRIGHTWAVE PARTNERS NAMECARD

Need to design a name card with an existing logo.

As we are professional corporate services provider our name card has to project a professional image.
Should be corporate, simple & professional.

Our corporate color is maroon red but not too dull.

Please refer to our website at www.brightwavepartners.com.sg

Would attach our logo herewith.

Front surface of namecard details:
BRIGHTWAVE PARTNERS PTE LTD
Registration No. 208731945K

Lowe Hui Ting CA (Singapore)
Director

Tel +65 6481 2957
Mobile +65 9172 3806
lowe@brightwavepartners.com.sg
www.brightwavepartners.com.sg

47 Palmer Lane
#07-14 Harbourlight Plaza
Singapore 274153

Back of namecard:-
OUR CORE SERVICES
Incorporation services
Corporate Secretarial Services
Accountancy service
Goods & Services Taxation
Corporate & Personal Taxation
Financial Reporting
Payroll Administration

AFFILIATES:
TRIVANTA CORPORATE SERVICES PTE LTD
BRIGHTWAVEREGISTRYPTE LTD
ORR MANAGEMENT SERVICES PTE LTD
DW LIM AND COMPANY PTE LTD
LEDGERWISE ACADEMY

```html
<!DOCTYPE html>
<html lang="en">
<head>
<meta charset="utf-8">
<title>Brightwave Partners Name Card</title>
<link href="https://fonts.googleapis.com/css2?family=Noto+Serif:wght@400;700&family=Tinos:wght@400;700&display=swap" rel="stylesheet">
<style>
  :root {
    --bg: #d4d4d4;
    --card-white: #ffffff;
    --brand-red: #d01f30;
    --ink: #1a1a1a;
    --paper-text: #ffffff;
  }
  * { margin: 0; padding: 0; box-sizing: border-box; }
  html, body { width: 900px; height: 1200px; overflow: hidden; }
  body { background: var(--bg); position: relative; font-family: "Tinos", "Times New Roman", serif; }

  .card {
    position: absolute; left: 113px; width: 673px; height: 396px;
    border-radius: 22px;
  }
  .card-front { top: 175px; background: var(--card-white); }
  .card-back { top: 631px; background: var(--brand-red); color: var(--paper-text); }

  .wordmark {
    position: absolute;
    font-family: "Tinos", "Times New Roman", serif;
    font-weight: 400; font-size: 47px; line-height: 46px;
    letter-spacing: -0.5px; text-transform: uppercase;
  }
  .card-front .wordmark { left: 35px; top: 52px; color: var(--brand-red); }
  .card-back .wordmark { left: 366px; top: 40px; color: var(--paper-text); }

  .holder { position: absolute; right: 40px; top: 60px; text-align: right; font-family: "Noto Serif", Georgia, serif; }
  .holder-name { font-weight: 700; font-size: 16.5px; color: var(--ink); line-height: 22px; }
  .holder-title { font-weight: 700; font-size: 14.5px; color: var(--brand-red); line-height: 22px; }

  .contact-list { position: absolute; left: 36px; top: 249px; list-style: none; font-size: 15.5px; color: var(--ink); }
  .contact-list li { display: flex; align-items: center; height: 19px; }
  .contact-list svg { width: 14px; height: 14px; margin-right: 10px; fill: none; stroke: var(--brand-red); stroke-width: 1.6; }

  .address { position: absolute; right: 40px; top: 249px; text-align: right; font-size: 15.5px; line-height: 19px; color: var(--ink); font-style: normal; }

  .rule { position: absolute; left: 37px; top: 360px; width: 395px; height: 1.5px; background: var(--brand-red); }
  .registration { position: absolute; right: 40px; top: 348px; font-size: 15px; color: var(--brand-red); }

  .section-title { position: absolute; left: 39px; font-family: "Noto Serif", Georgia, serif; font-weight: 700; font-size: 16.5px; }
  .services-title { top: 34px; }
  .affiliates-title { top: 231px; }

  .service-list { position: absolute; left: 39px; top: 58px; list-style: none; font-family: "Noto Serif", Georgia, serif; font-size: 14.5px; line-height: 21.2px; }
  .service-list li { display: flex; align-items: center; }
  .service-list li::before { content: ""; width: 10px; height: 10px; border-radius: 2px; background: var(--paper-text); margin-right: 8px; }

  .affiliate-list { position: absolute; left: 39px; top: 255px; list-style: none; font-family: "Noto Serif", Georgia, serif; font-size: 13.8px; line-height: 21.2px; }
</style>
</head>
<body>
  <section class="card card-front">
    <div class="wordmark">Brightwave<br>Partners</div>
    <div class="holder">
      <p class="holder-name">Lowe Hui Ting CA (Singapore)</p>
      <p class="holder-title">Director</p>
    </div>
    <ul class="contact-list">
      <li><svg viewBox="0 0 14 14"><path d="M3 1.5 L5 4.5 L3.8 5.8 Q5.5 8.8 8.2 10.2 L9.5 9 L12.5 11 L11 12.8 Q5 12 1.2 3 Z" fill="#d01f30" stroke="none"/></svg>+65 6481 2957</li>
      <li><svg viewBox="0 0 14 14"><rect x="2" y="1.5" width="10" height="11" rx="1.5"/><line x1="2" y1="10" x2="12" y2="10"/></svg>+65 9172 3806</li>
      <li><svg viewBox="0 0 14 14"><rect x="1.5" y="3" width="11" height="8" fill="#d01f30" stroke="none"/><polyline points="1.5,3 7,7.5 12.5,3" stroke="#fff" stroke-width="1.2"/></svg>lowe@brightwavepartners.com.sg</li>
      <li><svg viewBox="0 0 14 14"><circle cx="7" cy="7" r="5.5"/><ellipse cx="7" cy="7" rx="2.4" ry="5.5"/><line x1="1.5" y1="7" x2="12.5" y2="7"/></svg>www.brightwavepartners.com.sg</li>
    </ul>
    <address class="address">47 Palmer Lane<br>#07-14 Harbourlight Plaza<br>Singapore 274153</address>
    <div class="rule"></div>
    <p class="registration">Registration No. 208731945K</p>
  </section>

  <section class="card card-back">
    <h2 class="section-title services-title">OUR CORE SERVICES</h2>
    <ul class="service-list">
      <li>Incorporation services</li>
      <li>Corporate Secretarial Services</li>
      <li>Accountancy service</li>
      <li>Goods &amp; Services Taxation</li>
      <li>Corporate &amp; Personal Taxation</li>
      <li>Financial Reporting</li>
      <li>Payroll Administration</li>
    </ul>
    <h2 class="section-title affiliates-title">AFFILIATES</h2>
    <ul class="affiliate-list">
      <li>TRIVANTA CORPORATE SERVICES PTE LTD</li>
      <li>BRIGHTWAVEREGISTRYPTE LTD</li>
      <li>ORR MANAGEMENT SERVICES PTE LTD</li>
      <li>DW LIM AND COMPANY PTE LTD</li>
      <li>LEDGERWISE ACADEMY</li>
    </ul>
    <div class="wordmark">Brightwave<br>Partners</div>
  </section>
</body>
</html>
```